Exciting Personal Development Book Cover: FIND ZEN NOW!

Design a Book Cover for my personal development book.
Title: Find Zen Now!
Author: Marcus Telly
Tagline: A real-life solution to get unstuck and break free

My picture must make up the front cover as I need to build my brand and people should recognise me on book shelves. Bold and catchy. How you do it is up to you. There must be space for a short testimonial from a famous person who is currently reading my book. I uploaded a sample of what I made in Photoshop but I don't have design skills.

I've added a PDF of my book so you can read the chapter index and introduction to get a sense of the content.

Target Market(s)

Personal Development Self-Help Market

Industry/Entity Type

Personal Development

Font styles to use
Serif
Sans Serif

Requirements
Must have
• My picture as hero image on cover.
Nice to have
• Must have Title, Tagline and my author name. If possible ZEN stands for 'Zeal, Energy & Nerve' If there is a way to fit this somewhere great. If it's too much then it can go somewhere on the back.

```html
<!DOCTYPE html>
<html lang="en">
<head>
<meta charset="utf-8">
<title>Find Zen Now! – Book Cover Wrap</title>
<link rel="stylesheet" href="https://fonts.googleapis.com/css2?family=Anton&family=Roboto:wght@500;700;900&family=Roboto+Condensed:wght@700&display=swap">
<style>
  :root {
    --page: #ffffff;
    --slate-dark: #35383b;
    --slate-mid: #4a4d51;
    --slate-light: #9c9ea0;
    --title-navy: #213446;
    --accent-yellow: #d6c83c;
    --accent-yellow-deep: #b9ad2f;
    --ink-white: #ffffff;
    --ink-navy: #1e2a3a;
    --skin-tone: #b8927c;
    --shirt-white: #ececec;
  }
  * { box-sizing: border-box; margin: 0; padding: 0; }
  html, body { width: 1200px; height: 1200px; overflow: hidden; background: var(--page); }
  .canvas { position: relative; width: 1200px; height: 1200px; background: var(--page); }

  .wrap {
    position: absolute; left: 28px; top: 218px; width: 1146px; height: 766px;
    box-shadow: 4px 6px 6px rgba(0,0,0,0.35);
  }

  /* Back cover */
  .back-cover {
    position: absolute; left: 0; top: 0; width: 538px; height: 766px;
    background: linear-gradient(90deg, var(--slate-dark) 0%, #43464a 60%, var(--slate-dark) 100%);
  }
  .back-copy {
    position: absolute; left: 72px; top: 91px; width: 410px;
    font-family: "Roboto", sans-serif; font-weight: 500;
    font-size: 13.2px; line-height: 18.6px; color: var(--ink-white);
    text-align: justify;
  }
  .back-copy p + p { margin-top: 18px; }
  .back-band {
    position: absolute; left: 0; top: 564px; width: 538px; height: 144px;
    background: linear-gradient(180deg, var(--accent-yellow) 0%, var(--accent-yellow-deep) 100%);
    text-align: center; padding-top: 32px;
  }
  .back-quote {
    font-family: "Roboto", sans-serif; font-weight: 900; font-style: italic;
    font-size: 20px; line-height: 21px; color: var(--ink-white); text-transform: uppercase;
  }
  .back-quote .mark { font-size: 30px; vertical-align: -2px; }
  .back-attribution {
    margin-top: 9px; font-family: "Roboto", sans-serif; font-weight: 900;
    font-size: 19px; color: var(--ink-navy); text-transform: uppercase;
  }

  /* Spine */
  .spine {
    position: absolute; left: 538px; top: 0; width: 66px; height: 766px;
    background: var(--accent-yellow);
  }
  .spine-tagline {
    position: absolute; left: 32px; top: 56px; height: 260px;
    writing-mode: vertical-rl;
    font-family: "Roboto Condensed", sans-serif; font-weight: 700;
    font-size: 13px; line-height: 15px; letter-spacing: 0.6px;
    color: var(--title-navy); text-transform: uppercase; white-space: nowrap;
  }
  .spine-title {
    position: absolute; left: 14px; top: 318px; height: 200px;
    writing-mode: vertical-rl;
    font-family: "Anton", sans-serif; font-size: 34px; line-height: 38px;
    letter-spacing: 0.5px; color: var(--title-navy); white-space: nowrap;
  }
  .spine-author {
    position: absolute; left: 0; top: 520px; width: 66px; height: 190px;
    writing-mode: vertical-rl; display: flex; align-items: center; justify-content: center;
    font-family: "Roboto", sans-serif; font-weight: 700; font-size: 24px;
    color: var(--ink-white); letter-spacing: 1px; white-space: nowrap;
  }

  /* Front cover */
  .front-cover {
    position: absolute; left: 604px; top: 0; width: 542px; height: 766px;
    background: radial-gradient(ellipse 75% 70% at 62% 42%, var(--slate-light) 0%, #6e7174 45%, var(--slate-mid) 80%, #3d4043 100%);
    overflow: hidden;
  }
  .author-photo {
    position: absolute; left: 196px; top: 220px; width: 346px; height: 546px;
    background: linear-gradient(180deg, #2e2a28 0%, var(--skin-tone) 8%, var(--skin-tone) 26%, var(--shirt-white) 36%, #f4f4f4 100%);
    clip-path: polygon(120px 40px, 150px 5px, 212px 5px, 242px 40px, 246px 140px, 330px 175px, 346px 230px, 346px 546px, 0 546px, 0 240px, 40px 185px, 116px 150px);
  }
  .front-author {
    position: absolute; left: 62px; top: 50px;
    font-family: "Roboto", sans-serif; font-weight: 700; font-size: 56px;
    letter-spacing: 1.5px; color: var(--ink-white); white-space: nowrap; line-height: 1;
  }
  .front-title {
    position: absolute; left: 62px; top: 122px;
    font-family: "Anton", sans-serif; font-weight: 400; font-size: 126px; line-height: 132px;
    color: var(--title-navy); text-transform: uppercase; white-space: nowrap;
  }
  .front-title .highlight { color: var(--accent-yellow); }
  .front-tagline {
    position: absolute; left: 276px; top: 130px; width: 250px;
    font-family: "Roboto Condensed", sans-serif; font-weight: 700;
    font-size: 15px; line-height: 25px; color: var(--ink-white); text-transform: uppercase;
  }
  .front-ribbon { position: absolute; left: 0; top: 520px; width: 250px; height: 184px; }
  .front-testimonial {
    position: absolute; left: 22px; top: 556px; width: 210px;
    transform: rotate(-8deg); text-align: center;
  }
  .front-quote {
    font-family: "Roboto", sans-serif; font-weight: 900; font-size: 17px; line-height: 17px;
    color: var(--ink-white); text-transform: uppercase;
  }
  .front-attribution {
    margin-top: 8px; font-family: "Roboto", sans-serif; font-weight: 900;
    font-size: 18px; color: var(--ink-navy); text-transform: uppercase; white-space: nowrap;
  }
</style>
</head>
<body>
<div class="canvas">
  <div class="wrap">

    <section class="back-cover">
      <div class="back-copy">
        <p>Lorem ipsum dolor sit amet. Illum atque qui itaque saepe et vero porro eum aliquid sint qui dolores dolores ut dolor magnam. Qui aperiam accusamus in sunt et velit magni qui eveniet tempora et consectetur reprehenderit ea expedita molestiae! Aut nihil eaque et dolorum dolorem ut vero dolorum aut repudiandae sunt.</p>
        <p>Ut corporis maiores et repellendus possimus ut ipsam voluptas aut molestiae quisquam ex unde labore. Qui quae obcaecati ea molestiae esse et sint suscipit est voluptate vero!</p>
        <p>Aut iste dolor sit accusamus voluptates qui nobis quasi sit quae molestias quo veniam voluptas. Sit doloribus provident in eaque consequuntur et commodi impedit ad nemo rerum quo earum voluptatem? Et maiores voluptate est nostrum vero sit nesciunt Quis ut facere saepe et harum quia. Est mollitia natus eum qui-squam architecto sit veritatis delectus est minima internos est dolor quis aut fugiat explicabo nam dolorem doloremque. voluptatem? Et maiores voluptate est nostrum vero sit nesciunt Quis ut facere saepe et harum quia. Est mollitia natus eum qui-squam architecto sit veritatis delectus est minima internos est dolor quis aut fugiat explicabo nam dolorem doloremque.</p>
      </div>
      <div class="back-band">
        <p class="back-quote"><span class="mark">“</span>Lorem ipsum dolor sit amet,<br>consectetur adipiscing elit<span class="mark">”</span></p>
        <p class="back-attribution">Name Surname</p>
      </div>
    </section>

    <section class="spine">
      <p class="spine-tagline">A real-life solution to get<br>unstuck and break free</p>
      <p class="spine-title">FIND ZEN NOW!</p>
      <p class="spine-author">MARCUS TELLY</p>
    </section>

    <section class="front-cover">
      <div class="author-photo" role="img" aria-label="Portrait photo of author Marcus Telly, smiling in a white shirt with arms crossed"></div>
      <p class="front-author">MARCUS TELLY</p>
      <h1 class="front-title">Find<br><span class="highlight">Zen</span><br>Now!</h1>
      <p class="front-tagline">A real-life solution to get<br>unstuck and break free</p>
      <svg class="front-ribbon" viewBox="0 0 250 184" aria-hidden="true">
        <polygon points="0,42 248,4 248,144 0,180" fill="#d6c83c"/>
      </svg>
      <div class="front-testimonial">
        <p class="front-quote">“Lorem ipsum<br>dolor sit amet,<br>consectetur<br>adipiscing elit”</p>
        <p class="front-attribution">Name Surname</p>
      </div>
    </section>

  </div>
</div>
</body>
</html>
```